Certified Probate & Trust Postcard

Hi, I am looking for your assistance. I need a postcard design based on the following specifications. The postcard needs to be 6x9. Here are the specifications for the front and back sides. I also need help incorporating a section on the front of the postcard where I can write the name or names of the people I am addressing the postcard to, as well as a space on the back for the stamp and the receiver's address.

(revised 6/18/2025)
🖼️ FRONT SIDE

(Visual: A serene Bay Area home or warm, sunlit interior. Include Tessa’s headshot. Color palette: ivory, slate, soft gold.)

Headline:

You’ve Taken On So Much — Let Me Help with What Comes Next

Subhead:

Strategic Real Estate Guidance for Probate & Trust
Certified Probate & Trust Specialist | Serving the San Francisco Bay Area

⸻

đź“© BACK SIDE

Opening Quote (italicized):

“I lost both of my parents in 2020 — just weeks apart. That experience shaped how I serve every estate I touch.”

⸻

Main Body Copy:

My name is Tessa Harlow, and I’m a Certified Probate & Trust Specialist who works with families, attorneys, and fiduciaries to guide the real estate side of probate with structure, sensitivity, and strategy.

Whether you’re navigating this with legal support or filing in pro per, this process is layered — emotional, procedural, and often overwhelming. I provide a steady hand when everything else feels uncertain.

With over a decade of experience supporting executives at Corvana, Lumidel, and Dunmore Kass, I bring the same operational precision and discretion to every estate I manage. But I also bring empathy — because I’ve been in your shoes.

⸻

What I Offer — At No Upfront Cost to the Estate:
• Property clean-outs, inspections, and basic preparation — coordinated and covered
• Real estate strategy aligned with court timelines and estate goals
• Hands-on collaboration with attorneys or step-by-step guidance for independent petitioners
• Thoughtful communication that honors your time and your grief

Because real estate isn’t just business.
For you, it’s personal. For me, it’s both.

⸻

Call to Action (in soft gold frame or slate border):

If you’re managing a probate or trust estate and need support you can trust — let’s make this easier, together.
Snapgram: @itstessavoy | CareerNet: profilehub.example/in/tessahomeguide

Industry/Entity Type

Real Estate

Requirements
Must have
• Image needs to have a calm aesthetic (remember the person receiving is grieving) emphasis on luxury as we are looking to attract high end clients so not generic and something that is easily purchased from craftly
Nice to have
• need the following design scheme as it relates to color and font Primary Color Palette: 1. Ecru Stone (Soft Beige/Taupe) – #D7CCC0 • Evokes warmth, trust, and sophistication. 2. Slate Charcoal (Deep Neutral Gray) – #4A4A4A • Represents professionalism, authority, and reliability. Accent Colors: 3. Soft Gold (Understated Elegance) – #C2B280 • Adds a subtle richness without being flashy. 4. Powder White (Clean Background Base) – #FAF9F6 • Used for breathing room, high readability, and elegance. Typography/Callout Highlight Color: 5. Trust Blue (Soft Navy) – #3F4A5F • Often used for headers or key points to add credibility and depth. Tessa Harlow should be in cursive, readable and absolutely beautiful
Should not have
• No yellow, do not use ai on my image,

```html
<!DOCTYPE html>
<html lang="en">
<head>
<meta charset="utf-8">
<title>Certified Probate &amp; Trust Postcard</title>
<link href="https://fonts.googleapis.com/css2?family=Barlow+Condensed:wght@400;500;600;700&family=Great+Vibes&display=swap" rel="stylesheet">
<style>
:root{
  --slate-navy:#434B5F;
  --soft-gold:#C2B280;
  --powder-white:#FAF9F6;
  --ecru-stone:#D7CCC0;
  --ink:#3F4A5F;
  --rule:#6b7285;
  --address-rule:#ece6d2;
  --stage:#000;
  --paper:#fff;
}
*{margin:0;padding:0;box-sizing:border-box}
html,body{width:1011px;height:1200px;overflow:hidden;background:var(--stage)}
body{position:relative;font-family:"Barlow Condensed",sans-serif;color:var(--ink)}
.card{position:absolute;left:168px;width:676px;overflow:hidden}
.card-front{top:130px;height:451px;background:var(--powder-white)}
.card-back{top:619px;height:450px;background:var(--paper)}

/* front */
.front-topband{position:absolute;left:0;top:0;width:100%;height:37px;background:var(--slate-navy)}
.front-photo{position:absolute;left:0;top:37px;width:100%;height:324px;
  background:linear-gradient(180deg,#fbfaf8 0%,#f3f1ec 38%,#e7e2da 60%,#c9cfc0 72%,#b9bfa6 85%,#a99578 100%)}
.front-photo .window{position:absolute;left:349px;top:118px;width:312px;height:206px;
  background:linear-gradient(160deg,#cfe0ef 0%,#9fb48e 45%,#6f8a5e 100%);opacity:.75}
.salutation{position:absolute;left:238px;top:19px;width:200px;height:34px;border-radius:17px;
  background:var(--powder-white);border:1px solid var(--ecru-stone);
  font-family:"Great Vibes",cursive;font-size:21px;color:var(--ink);text-align:center;line-height:33px}
.headline{position:absolute;left:0;top:59px;width:100%;text-align:center;font-size:40px;line-height:41px;color:var(--ink);font-weight:400;padding-left:8px}
.headline strong{font-weight:700}
.ribbon{position:absolute;left:147px;top:149px;width:382px;height:24px}
.ribbon svg{position:absolute;inset:0}
.ribbon span{position:relative;display:block;text-align:center;font-size:17.5px;line-height:24px;color:var(--ink)}
.front-band{position:absolute;left:0;top:361px;width:100%;height:90px;background:var(--slate-navy)}
.headshot-front{position:absolute;left:274px;top:290px;width:128px;height:128px;border-radius:50%;
  background:radial-gradient(circle at 50% 45%,#8a6a55 0,#5a4438 40%,#2c2a2e 70%,#a9a197 100%);border:3px solid var(--ecru-stone)}
.credentials{position:absolute;left:20px;top:376px;font-size:15px;line-height:16px;color:var(--soft-gold)}
.band-rule-left{position:absolute;left:0;top:413px;width:266px;height:1px;background:var(--rule)}
.tagline{position:absolute;left:20px;top:418px;font-size:12px;line-height:13.5px;color:var(--powder-white)}
.signature{position:absolute;left:282px;top:420px;width:120px;text-align:center;font-family:"Great Vibes",cursive;font-size:23px;line-height:26px;color:var(--soft-gold);white-space:nowrap}
.cta{position:absolute;left:425px;top:373px;font-size:11.8px;line-height:15.5px;color:var(--powder-white)}
.band-rule-right{position:absolute;left:543px;top:413px;width:133px;height:1px;background:var(--rule)}
.social{position:absolute;left:425px;top:421px;font-size:11px;line-height:14px;color:var(--powder-white);display:flex;gap:7px;align-items:center;white-space:nowrap}
.social i{display:inline-block;width:8px;height:8px;border-radius:50%;background:var(--soft-gold);margin-right:3px}

/* back */
.back-message{position:absolute;left:0;top:0;width:365px;height:450px;background:var(--powder-white)}
.quote-shape{position:absolute;left:0;top:0}
.quote{position:absolute;left:36px;top:23px;width:300px;font-size:17.5px;line-height:20.3px;color:var(--powder-white);white-space:nowrap}
.photo-pill{position:absolute;left:37px;top:131px;width:33px;height:169px;border-radius:17px 17px 0 0;background:var(--soft-gold)}
.headshot-back{position:absolute;left:7px;top:169px;width:84px;height:84px;border-radius:50%;
  background:radial-gradient(circle at 50% 45%,#8a6a55 0,#5a4438 40%,#2c2a2e 75%,#d8d2c8 100%)}
.bio{position:absolute;left:93px;top:135px;width:244px;font-size:9.6px;line-height:12.5px;color:var(--ink);text-align:justify}
.bio p{margin-bottom:12.5px}
.offer-rule{position:absolute;left:62px;width:217px;height:1px;background:var(--ecru-stone)}
.offer-title{position:absolute;left:28px;top:328px;font-size:17px;line-height:22px;font-weight:600;color:var(--ink);white-space:nowrap}
.offer-item{position:absolute;display:flex;gap:4px;font-size:9px;line-height:10px;color:var(--ink)}
.offer-item svg{flex:none;margin-top:2px}
.offer-item span{width:128px}
.stamp-box{position:absolute;left:571px;top:28px;width:78px;height:78px;border:1px solid var(--soft-gold)}
.address-line{position:absolute;left:397px;width:222px;height:1px;background:var(--address-rule)}
</style>
</head>
<body>

<section class="card card-front">
  <div class="front-topband"></div>
  <div class="front-photo" role="img" aria-label="Bright sunlit living room with plants, pale blue armchairs and sliding glass doors opening to a green Bay Area view">
    <div class="window"></div>
  </div>
  <div class="salutation">Dear Mr. Whitaker</div>
  <h1 class="headline">You’ve Taken On So Much — <strong>Let<br>Me Help with What Comes Next</strong></h1>
  <div class="ribbon">
    <svg width="382" height="24" viewBox="0 0 382 24"><path d="M0 0H382L372 12L382 24H0L10 12Z" fill="#C2B280"/></svg>
    <span>Strategic Real Estate Guidance for Probate &amp; Trust</span>
  </div>
  <div class="front-band"></div>
  <div class="headshot-front" role="img" aria-label="Headshot of Tessa Harlow"></div>
  <p class="credentials">Certified Probate &amp; Trust Specialist<br>Serving the San Francisco Bay Area</p>
  <div class="band-rule-left"></div>
  <p class="tagline">Because real estate isn't just business.<br>&nbsp;For you, it's personal. For me, it's both.</p>
  <div class="signature">Tessa Harlow</div>
  <p class="cta">If you’re managing a probate or trust estate and need<br>support you can trust — let's make this easier, together.</p>
  <div class="band-rule-right"></div>
  <p class="social"><span><i></i>@itstessavoy</span><span><i></i>profilehub.example/in/tessahomeguide</span></p>
</section>

<section class="card card-back">
  <div class="back-message"></div>
  <svg class="quote-shape" width="380" height="135" viewBox="0 0 380 135">
    <path d="M225 0H340C372 0 378 30 365 65C350 105 320 127 275 126C320 120 345 95 352 62C360 28 345 2 300 0Z" fill="#C2B280"/>
    <path d="M0 0H330C362 0 365 35 350 70C335 105 305 125 265 126Q130 120 0 97Z" fill="#434B5F"/>
  </svg>
  <p class="quote">“I lost both of my parents in 2020 — just<br>weeks apart. That experience shaped how<br>I serve every estate I touch.”</p>
  <div class="photo-pill"></div>
  <div class="headshot-back" role="img" aria-label="Headshot of Tessa Harlow"></div>
  <div class="bio">
    <p>My name is Tessa Harlow, and I'm a Certified Probate &amp; Trust Specialist who works with families, attorneys, and fiduciaries to guide the real estate side of probate with structure, sensitivity, and strategy.</p>
    <p>Whether you're navigating this with legal support or filing in pro per, this process is layered — emotional, procedural, and often overwhelming. I provide a steady hand when everything else feels uncertain.</p>
    <p>With over a decade of experience supporting executives at Corvana, Lumidel, and Dunmore Kass, I bring the same operational precision and discretion to every estate I manage. But I also bring empathy — because I've been in your shoes.</p>
  </div>
  <div class="offer-rule" style="top:323px"></div>
  <h2 class="offer-title">What I Offer — At No Upfront Cost to the Estate:</h2>
  <div class="offer-rule" style="top:355px"></div>
  <div class="offer-item" style="left:16px;top:366px">
    <svg width="18" height="18" viewBox="0 0 18 18" fill="none" stroke="#C2B280" stroke-width="1.2"><path d="M2 9L9 3L16 9M4 8V16H14V8"/><circle cx="9" cy="11" r="2.5"/></svg>
    <span>Property clean-outs, inspections, and basic preparation — coordinated and covered</span>
  </div>
  <div class="offer-item" style="left:16px;top:407px">
    <svg width="18" height="18" viewBox="0 0 18 18" fill="none" stroke="#C2B280" stroke-width="1.2"><rect x="2" y="3" width="14" height="9"/><path d="M6 12L4 17M12 12L14 17M5 9L8 6L10 8L13 5"/></svg>
    <span>Real estate strategy aligned with court timelines and estate goals</span>
  </div>
  <div class="offer-item" style="left:176px;top:366px">
    <svg width="18" height="18" viewBox="0 0 18 18" fill="none" stroke="#C2B280" stroke-width="1.2"><path d="M4 2H12L15 5V16H4Z"/><path d="M6 7H12M6 10H12M6 13H10"/></svg>
    <span>Hands-on collaboration with attorneys or step-by-step guidance for independent petitioners</span>
  </div>
  <div class="offer-item" style="left:176px;top:407px">
    <svg width="18" height="18" viewBox="0 0 18 18" fill="none" stroke="#C2B280" stroke-width="1.2"><path d="M3 4H15V12H8L5 15V12H3Z"/><circle cx="6.5" cy="8" r=".6"/><circle cx="9" cy="8" r=".6"/><circle cx="11.5" cy="8" r=".6"/></svg>
    <span>Thoughtful communication that honors your time and your grief</span>
  </div>
  <div class="stamp-box"></div>
  <div class="address-line" style="top:176px"></div>
  <div class="address-line" style="top:208px"></div>
  <div class="address-line" style="top:240px"></div>
  <div class="address-line" style="top:271px"></div>
  <div class="address-line" style="top:303px"></div>
</section>

</body>
</html>
```